Family Photography A5 Invitation to prospective clients

A restaurant will give me public space at their entrance to promote my family photography. I need an A5 vertical layout design for a card to 'invite' potential clients to call me. I am a portrait photographer in Perth, Western Australia. The A5 cards will be taken away by potential clients. They are encouraged to call the studio to register their interest with a view to having a very beautiful family portrait in the studio or on location. This will save the family $250 because the fee will be waived. Locations for photography can include a sunset at the famous Tarrington Beach or parks in the Western Suburbs of Perth. Prefer Indesign work file so that I can change images for reprints later. Will be happy to give extra ongoing work to the successful designer on future projects. I'm happy to take positional images in the design and change them later.

Target Market(s)

Women mainly in the 30 to 45 years age group

Industry/Entity Type

Restaurant

Font styles to use
Sans Serif

Requirements
Must have
• Call to action and lively design that gets attention. Prefer to have some similarity with style of web site wrenlightstudio.com.au
Nice to have
• Prefer not to have the look of fake 'competitions' but rather an invitation to have a beautiful experience and with the opportunity to purchase a beautiful piece of art that celebrates their family. See word doc for previous idea with 'win a portrait...' Some of the words might be useful. More here... Dean Marlow’s photography hangs on thousands of walls in Perth’s homes. His family portraits are not so much photographs as works of art, each one perfect in its own way, a unique interplay of light, shade, colour and composition. They’re the ones that make people say more than just, ‘Oh, nice’. They make people linger and say, ‘Wow, amazing!’.
Should not have
• Avoid too much emphasis on cost. I am not competing on cost, but rather trying to inspire the potential client. See word doc for previous idea with 'win a portrait...' Some of the words might be useful.

```html
<!DOCTYPE html>
<html lang="en">
<head>
<meta charset="utf-8">
<title>Wrenlight Studio – Portrait Session Invitation</title>
<link href="https://fonts.googleapis.com/css2?family=Quicksand:wght@400;500&display=swap" rel="stylesheet">
<style>
  :root {
    --frame: #000000;
    --paper: #ffffff;
    --taupe: #aaa594;
    --ink: #4a4a4a;
    --accent: #a7a18b;
    --ring: #8c8c8c;
    --sky-top: #e9d2b4;
    --sky-mid: #d7a98a;
    --sea: #8d9aa0;
  }
  html, body {
    margin: 0;
    padding: 0;
    width: 939px;
    height: 1200px;
    overflow: hidden;
    background: var(--frame);
  }
  .card {
    position: absolute;
    left: 26px;
    top: 26px;
    width: 887px;
    height: 1148px;
    background: var(--paper);
    overflow: hidden;
    font-family: "Quicksand", sans-serif;
    color: var(--ink);
  }
  .side-band {
    position: absolute;
    left: 0;
    top: 0;
    width: 152px;
    height: 100%;
    background: var(--taupe);
  }
  .foot-band {
    position: absolute;
    right: 0;
    bottom: 0;
    width: 333px;
    height: 32px;
    background: var(--taupe);
  }
  .brand-seal {
    position: absolute;
    left: 26px;
    top: 27px;
    width: 191px;
    height: 191px;
    border-radius: 50%;
    background: var(--paper);
    display: flex;
    align-items: center;
    justify-content: center;
    text-align: center;
  }
  .brand-name {
    font-size: 24px;
    font-weight: 500;
    line-height: 29px;
    color: var(--ring);
  }
  .portrait-slot {
    position: absolute;
    left: 20px;
    top: 300px;
    width: 112px;
    height: 460px;
    border: 4px solid var(--paper);
    box-sizing: border-box;
    background: linear-gradient(180deg, var(--sky-top) 0%, var(--sky-mid) 55%, var(--sea) 100%);
  }
  .letter {
    position: absolute;
    left: 257px;
    top: 84px;
    width: 602px;
    font-size: 16.6px;
    line-height: 30.4px;
    letter-spacing: -0.1px;
  }
  .letter p {
    margin: 0 0 30.4px 0;
  }
  .signature {
    color: var(--accent);
    margin: 0;
  }
</style>
</head>
<body>
  <main class="card">
    <div class="side-band"></div>
    <div class="foot-band"></div>

    <div class="brand-seal">
      <span class="brand-name">Wrenlight<br>Studio</span>
    </div>

    <div class="portrait-slot" role="img" aria-label="Family portrait at sunset on Tarrington Beach"></div>

    <article class="letter">
      <p>Hi there,</p>
      <p>You’re warmly invited… While you enjoy Corvina Restaurant in North Tarrington, imagine a portrait of your family that makes people stop, linger and say, ‘Wow, amazing!’ – a true work of art for your walls.</p>
      <p>Dean Marlow’s photography hangs on thousands of walls in Perth homes. Each portrait is a unique interplay of light, shade, colour and composition.</p>
      <p>This is your opportunity to own the most beautiful photographic art of yourself and your loved ones. We’re looking forward to giving you the experience of a photography session you’ll never forget.</p>
      <p>You’ll be asked to imagine your perfect backdrop. Will it be a sunset on Tarrington Beach? A park full of flowers and greenery? Or perhaps a creative black and white session at our North Harbourside studio? The choice is yours.</p>
      <p>After your session, we’ll arrange a cinema experience to highlight the many ways of presenting your beautiful images. We guarantee that your images will reflect personality, humour and love. Like so many of our clients, you’ll probably return in future years because our work really does keep on giving.</p>
      <p>See yourself in a new light. All you need do now is pick up the phone and call Dean to reserve your session. How easy is that?</p>
      <p>Warmest wishes,</p>
      <p class="signature">Dean Marlow<br>Phone 6400 7382</p>
    </article>
  </main>
</body>
</html>
```